Fundraising Study Day East of England. Lift the January blues!

A flyer to advertise a fundraising event of lectures for dental hygienists and therapists in support of the exemption campaign. Currently dental hygienists and therapists require a prescription to deliver certain treatment or recommend certain toothpastes. If we are successful in the campaign we will be able to treat patients without these restrictions.

Industry/Entity Type

Dental

```html
<!DOCTYPE html>
<html lang="en">
<head>
<meta charset="utf-8">
<title>Fundraising Study Day – East of England</title>
<link rel="stylesheet" href="https://fonts.googleapis.com/css2?family=Bebas+Neue&family=Lato:wght@400;700;900&display=swap">
<style>
  :root{
    --orange:#f05a0f;
    --navy:#0b4382;
    --ink:#2b2b2b;
    --text:#333;
    --dark-row:#4a4a4a;
    --light-row:#dedede;
    --band:#f1f1f1;
    --page-bg:#e6e6e6;
    --white:#fff;
  }
  *{box-sizing:border-box;margin:0;padding:0}
  html,body{width:1200px;height:1200px;overflow:hidden;background:var(--page-bg)}
  body{font-family:'Lato',sans-serif;color:var(--text);position:relative}
  .flyer{position:absolute;left:190px;top:24px;width:820px;height:1152px;background:var(--white);overflow:hidden;box-shadow:0 4px 18px rgba(0,0,0,.18)}
  .shapes,.photo{position:absolute;left:0;top:0}
  .headline{position:absolute;left:32px;top:56px}
  .headline__fund{font-family:'Bebas Neue',sans-serif;font-size:62px;line-height:.9;color:var(--orange);letter-spacing:.5px}
  .headline__study{font-family:'Lato',sans-serif;font-weight:700;font-size:30px;line-height:1;color:var(--navy);margin-top:0}
  .region-pill{position:absolute;left:32px;top:150px;width:226px;height:42px;background:var(--orange);border-radius:7px;color:var(--white);font-size:28px;line-height:42px;padding-left:8px;box-shadow:0 3px 4px rgba(0,0,0,.2)}
  .tagline{position:absolute;left:32px;top:206px;font-size:31px;line-height:1.1;font-weight:700;color:#3a3a3a}
  .tagline__big{position:absolute;left:32px;top:248px;font-family:'Bebas Neue',sans-serif;font-size:80px;line-height:.8;color:var(--navy)}
  .intro{position:absolute;left:33px;top:318px;width:480px;font-size:14px;line-height:17.7px;color:#3a3a3a}
  .info-band{position:absolute;left:4px;top:437px;width:766px;height:96px;background:var(--band);border-top:2px solid #e2e2e2;border-bottom:2px solid #e2e2e2}
  .info{position:absolute;top:475px;display:flex;align-items:flex-start;gap:8px;font-size:19px;line-height:23px;color:var(--ink);white-space:nowrap}
  .info--venue{left:36px;font-weight:700}
  .info--date{left:296px}
  .info--cost{left:512px;font-weight:700;font-size:22px;align-items:center;top:478px}
  .info--cost .price{color:var(--navy)}
  .schedule{position:absolute;left:27px;top:567px;display:grid;grid-template-columns:106px 254px 117px 283px;grid-template-rows:76px 130px 54px 147px;gap:3px;border-radius:14px;overflow:hidden;background:var(--white)}
  .cell{padding:8px 12px;font-size:12.5px;line-height:16px}
  .cell b{font-weight:700}
  .cell--dark{background:var(--dark-row);color:var(--white)}
  .cell--light{background:var(--light-row);color:#222}
  .cell--time{font-family:'Bebas Neue',sans-serif;font-size:23px;line-height:1;white-space:nowrap;letter-spacing:0;color:var(--orange);display:flex;align-items:center;padding:0 8px}
  .cell--time.top{align-items:flex-start;padding-top:14px}
  .cell--just{text-align:justify}
  .cell--mid{display:flex;align-items:center}
</style>
</head>
<body>
<main class="flyer">
  <svg class="shapes" width="820" height="1152" viewBox="0 0 820 1152" aria-hidden="true">
    <polygon points="242,0 448,0 350,98" fill="#0b4382"/>
  </svg>
  <svg class="photo" width="820" height="1152" viewBox="0 0 820 1152" role="img" aria-label="Photo of a dental patient in the chair with gloved hands holding dental instruments">
    <defs>
      <linearGradient id="photoTone" x1="0" y1="0" x2="1" y2="1">
        <stop offset="0" stop-color="#b9c7d8"/>
        <stop offset=".5" stop-color="#d7b3a0"/>
        <stop offset="1" stop-color="#6f86c6"/>
      </linearGradient>
    </defs>
    <polygon points="360,125 484,0 820,0 820,242 645,408" fill="url(#photoTone)"/>
  </svg>

  <div class="headline">
    <div class="headline__fund">Fundraising</div>
    <div class="headline__study">STUDY DAY</div>
  </div>
  <div class="region-pill">East of England</div>
  <div class="tagline">Lift the January</div>
  <div class="tagline__big">BLUES!</div>
  <p class="intro">A fundraising event to support our exemptions project. The day will consist of a series of presentations ranging from the new ECPD to new technologies. The aim, being to enhance our learning and raise funds to support the exemptions campaign. The speaker line includes some of the UK and Irelands most respected dental professionals in our field.</p>

  <div class="info-band"></div>
  <svg class="shapes" width="820" height="1152" viewBox="0 0 820 1152" aria-hidden="true">
    <polygon points="820,264 672,417 820,573" fill="#f05a0f"/>
  </svg>

  <div class="info info--venue">
    <svg width="20" height="26" viewBox="0 0 20 26" aria-hidden="true"><path d="M10 1a8 8 0 0 0-8 8c0 6 8 15 8 15s8-9 8-15a8 8 0 0 0-8-8z" fill="none" stroke="#f05a0f" stroke-width="2"/><circle cx="10" cy="9" r="3" fill="none" stroke="#f05a0f" stroke-width="2"/></svg>
    <div>Ashby Hotel Meadow Way<br>Elmford EL4 2QT</div>
  </div>
  <div class="info info--date">
    <svg width="26" height="26" viewBox="0 0 26 26" aria-hidden="true"><rect x="2" y="4" width="22" height="20" rx="2" fill="none" stroke="#f05a0f" stroke-width="2"/><rect x="2" y="4" width="22" height="5" fill="#f05a0f"/><g fill="#f05a0f"><rect x="6" y="12" width="3" height="3"/><rect x="11" y="12" width="3" height="3"/><rect x="16" y="12" width="3" height="3"/><rect x="6" y="17" width="3" height="3"/><rect x="11" y="17" width="3" height="3"/></g></svg>
    <div>Fri 19 January 2018<br>09:00 – 16:30 GMT</div>
  </div>
  <div class="info info--cost">
    <svg width="28" height="28" viewBox="0 0 28 28" aria-hidden="true"><circle cx="14" cy="14" r="13" fill="#f05a0f"/><circle cx="14" cy="14" r="9.5" fill="none" stroke="#fff" stroke-width="1.5"/><text x="14" y="19" text-anchor="middle" font-family="Lato,sans-serif" font-weight="700" font-size="13" fill="#fff">£</text></svg>
    <div>Cost - <span class="price">£101.48</span></div>
  </div>

  <section class="schedule">
    <div class="cell cell--dark cell--time">9.30 - 10.15</div>
    <div class="cell cell--dark"><b>Helen Marsh</b>: Immediate past president of the DHTA will be updating us on all things ECPD</div>
    <div class="cell cell--dark cell--time top">12 - 1400</div>
    <div class="cell cell--dark" style="padding-top:22px">Lunch</div>

    <div class="cell cell--light cell--time">10.15 - 11.00</div>
    <div class="cell cell--light cell--just"><b>Laura Pennick</b>: Will provide an update on teeth whiteing and explain how social media has impacted her business <b>Claire Danvers</b>: Our internationally acclaimed speaker will update our knowledge of periodontal disease and nutrition and new technologies.</div>
    <div class="cell cell--light cell--time top">14 - 15.00</div>
    <div class="cell cell--light" style="padding-top:16px"><b>Sam Ridley</b>: Save your back. All things posture.</div>

    <div class="cell cell--dark cell--time">11.00 - 11.30</div>
    <div class="cell cell--dark cell--mid">Break</div>
    <div class="cell cell--dark cell--time">15.00 - 15.30</div>
    <div class="cell cell--dark cell--mid">Break</div>

    <div class="cell cell--light cell--time">11.30 - 13.00</div>
    <div class="cell cell--light cell--just"><b>Niamh Corrigan &amp; Rachel Tilney</b>: Will be providing a combined presentation on 'Scaling your business' and start to finish SonicFlow techniques. The aim being to build our business with effective communications, systems and protocols. This sessions promises audience participation!</div>
    <div class="cell cell--light cell--time top" style="padding-top:40px">15.30 - 16.30</div>
    <div class="cell cell--light" style="padding-top:18px"><b>Claire Danvers</b>: Our internationally acclaimed speaker will update our knowledge of periodontal disease and nutrition and new technologies.</div>
  </section>

  <svg class="photo" width="820" height="1152" viewBox="0 0 820 1152" role="img" aria-label="Photo of a cheerful group of dental team members raising their arms with thumbs up">
    <defs>
      <linearGradient id="teamTone" x1="0" y1="0" x2="0" y2="1">
        <stop offset="0" stop-color="#ffffff" stop-opacity="0"/>
        <stop offset=".35" stop-color="#c9cfd8"/>
        <stop offset="1" stop-color="#5f7ea6"/>
      </linearGradient>
    </defs>
    <rect x="152" y="982" width="524" height="170" fill="url(#teamTone)"/>
  </svg>
</main>
</body>
</html>
```